Every Drawer Neatly Sorted or EDN Organized needs a business card design. EDN Organized is a professi

We need a business card design that is clean, sharp and conveys a sense of organization. I already have a logo.

Target Market(s)

Families (specifically mothers), small business owners, parents, seniors

Industry/Entity Type

Business

Contact Information for Business Card

My website is www.ednorganized-example.com and my Facebook page is http://www.socialpage-example.com/everydrawerneatlysorted. The phone number is 555-418-2706 and I want to be listed as Miriel O. Dunsford, Owner

Requirements
Must have
• My logo.

```html
<!DOCTYPE html>
<html lang="en">
<head>
<meta charset="utf-8">
<title>EDN Organized – Business Card</title>
<link href="https://fonts.googleapis.com/css2?family=Montserrat:wght@400&family=Arimo:wght@400;700&display=swap" rel="stylesheet">
<style>
  :root {
    --backdrop: #e9e6e1;
    --card-white: #ffffff;
    --card-black: #050505;
    --brand-blue: #1a7fd8;
    --ink: #1b1b1b;
    --text-light: #ffffff;
  }
  * { box-sizing: border-box; margin: 0; padding: 0; }
  html, body {
    width: 1200px; height: 950px; overflow: hidden;
    background: var(--backdrop);
  }
  .stage { position: relative; width: 1200px; height: 950px; }
  .card {
    position: absolute; left: 250px; width: 700px; height: 400px;
    box-shadow: 0 10px 30px rgba(0,0,0,0.25);
    overflow: hidden;
  }
  /* Front */
  .card--front { top: 45px; background: var(--card-white); }
  .front-brand {
    position: absolute; left: 110px; top: 150px;
    display: flex; align-items: center; gap: 18px;
  }
  .brand-dot {
    width: 26px; height: 26px; border-radius: 50%;
    background: var(--brand-blue); flex: none;
  }
  .brand-name {
    font-family: "Montserrat", sans-serif; font-weight: 400;
    font-size: 31px; letter-spacing: 3px; color: var(--ink);
    white-space: nowrap;
  }
  .front-web {
    position: absolute; left: 113px; top: 232px;
    font-family: "Montserrat", sans-serif; font-weight: 400;
    font-size: 15px; letter-spacing: 5px; color: var(--ink);
  }
  /* Back */
  .card--back { top: 505px; background: var(--card-black); }
  .edge-strip {
    position: absolute; left: 0; top: 0; width: 22px; height: 190px;
    background: var(--card-white);
  }
  .back-brand {
    position: absolute; left: 90px; top: 88px;
    display: flex; align-items: center; gap: 16px;
  }
  .brand-square {
    width: 30px; height: 30px; background: var(--brand-blue); flex: none;
  }
  .back-brand-name {
    font-family: "Montserrat", sans-serif; font-weight: 400;
    font-size: 34px; letter-spacing: 2px; color: var(--text-light);
    white-space: nowrap;
  }
  .contact-panel {
    position: absolute; left: 365px; top: 150px; right: 0; height: 215px;
    background: var(--brand-blue);
    border-radius: 42px 0 0 42px;
    padding: 26px 0 0 50px;
    color: var(--text-light);
    font-family: "Arimo", sans-serif;
  }
  .person-name { font-weight: 700; font-size: 21px; letter-spacing: 0.5px; white-space: nowrap; }
  .person-role { font-weight: 700; font-size: 13px; margin-top: 6px; letter-spacing: 0.5px; }
  .contact-list { list-style: none; margin-top: 26px; }
  .contact-list li {
    display: flex; align-items: center; gap: 9px;
    font-size: 16px; line-height: 23px; white-space: nowrap;
  }
  .contact-list svg { width: 14px; height: 14px; flex: none; }
</style>
</head>
<body>
<main class="stage">
  <section class="card card--front">
    <div class="front-brand">
      <span class="brand-dot"></span>
      <span class="brand-name">Every Drawer Neatly Sorted</span>
    </div>
    <p class="front-web">www.ednorganized-example.com</p>
  </section>

  <section class="card card--back">
    <div class="edge-strip"></div>
    <div class="back-brand">
      <span class="brand-square"></span>
      <span class="back-brand-name">EDN Organized</span>
    </div>
    <div class="contact-panel">
      <p class="person-name">MIRIEL O. DUNSFORD</p>
      <p class="person-role">OWNER</p>
      <ul class="contact-list">
        <li>
          <svg viewBox="0 0 16 16" aria-hidden="true"><path fill="currentColor" d="M3.6 1.5l2.3 2.6-1.3 1.8c.9 2 2.5 3.6 4.5 4.5l1.8-1.3 2.6 2.3-1.4 2.3C6.9 13.5 2.5 9.1 1.3 3z"/></svg>
          <span>555-418-2706</span>
        </li>
        <li>
          <svg viewBox="0 0 16 16" aria-hidden="true"><circle cx="8" cy="8" r="6.5" fill="none" stroke="currentColor" stroke-width="1.6"/><path d="M1.5 8h13M8 1.5c3 3.5 3 9.5 0 13M8 1.5c-3 3.5-3 9.5 0 13" fill="none" stroke="currentColor" stroke-width="1.2"/></svg>
          <span>www.ednorganized-example.com</span>
        </li>
        <li>
          <svg viewBox="0 0 16 16" aria-hidden="true"><rect x="1.5" y="1.5" width="13" height="13" rx="2" fill="currentColor"/></svg>
          <span>everydrawerneatlysorted</span>
        </li>
      </ul>
    </div>
  </section>
</main>
</body>
</html>
```